New Stationery Design Project

We got a project done from you for Corvanta stationary design. We have changed the name of the company from Corvanta to Brelix.
So we want to redesign our stationay.
We are a VOIP, hosted pbx, and cloud services provider. Clients are mostly hotels, offices, business etc. needing phone services.
Our Slogan is : "Clear calls, fair prices, every day"
the logo has to be changed from Corvanta to Brelix
Business address is
4127 Harlow Pkwy, suite 410
Marlow TX 75318
Phone: 555-014-2297
Fax: 555-014-2297
Website: Brelix.example
Industry/Entity Type
Business
Look and feel
Each slider illustrates characteristics of the customer's brand and the style your logo design should communicate.

```html
<!DOCTYPE html>
<html lang="en">
<head>
<meta charset="utf-8">
<title>Brelix Stationery</title>
<link rel="stylesheet" href="https://fonts.googleapis.com/css2?family=Montserrat:ital,wght@0,400;0,500;0,600;1,400&display=swap">
<style>
  :root {
    --bg: #ececec;
    --paper: #ffffff;
    --paper-shade: #f3f3f3;
    --charcoal: #363636;
    --ink: #3b3b3b;
    --muted: #8a8a8a;
    --light-text: #d9d9d9;
    --c-magenta: #e2257d;
    --c-yellow: #f6c514;
    --c-green: #7cbf3a;
    --c-blue: #1f8fd6;
    --c-orange: #f07a1f;
    --c-purple: #8b3fa8;
  }
  * { box-sizing: border-box; margin: 0; padding: 0; }
  html, body {
    width: 1200px; height: 859px; overflow: hidden;
    background: var(--bg);
    font-family: "Montserrat", Arial, sans-serif;
    color: var(--ink);
  }
  .sheet {
    position: absolute;
    box-shadow: 0 2px 6px rgba(0,0,0,0.12);
    overflow: hidden;
  }
  .bubble-band {
    background: linear-gradient(90deg, var(--c-magenta), var(--c-yellow) 25%, var(--c-green) 45%, var(--c-blue) 65%, var(--c-orange) 82%, var(--c-purple));
  }
  .brand-name {
    font-weight: 600;
    letter-spacing: 0.18em;
    text-transform: uppercase;
    line-height: 1;
    white-space: nowrap;
  }
  .slogan {
    font-style: italic;
    font-weight: 400;
    color: var(--muted);
    white-space: nowrap;
  }
  .dark-band {
    position: absolute; left: 0; right: 0; bottom: 0;
    background: var(--charcoal);
    color: var(--light-text);
    display: flex; align-items: center;
  }
  .band-text { white-space: nowrap; overflow: hidden; }

  /* Letterhead */
  .letterhead { left: 50px; top: 140px; width: 410px; height: 580px; background: var(--paper); }
  .letterhead .brand { position: absolute; top: 50px; left: 0; right: 0; text-align: center; }
  .letterhead .brand-name { font-size: 26px; color: var(--charcoal); }
  .letterhead .slogan { font-size: 10px; margin-top: 7px; }
  .letterhead .dark-band { height: 30px; font-size: 6px; letter-spacing: 0.02em; }
  .letterhead .band-start { width: 52px; height: 100%; }
  .letterhead .band-text { flex: 1; padding: 0 12px; }
  .letterhead .band-end { width: 52px; height: 100%; }

  /* Folder */
  .folder { left: 490px; top: 140px; width: 410px; height: 580px; background: var(--charcoal); }
  .folder .brand { position: absolute; top: 150px; left: 0; right: 0; text-align: center; }
  .folder .mark { width: 22px; height: 22px; margin: 0 auto 16px; border-radius: 50%; }
  .folder .brand-name { font-size: 30px; color: var(--paper); }
  .folder .slogan { font-size: 11px; margin-top: 9px; color: var(--light-text); }
  .folder .web { position: absolute; bottom: 40px; left: 0; right: 0; text-align: center; font-size: 9px; color: var(--light-text); letter-spacing: 0.05em; }

  /* Business cards */
  .card { width: 220px; height: 126px; }
  .card-front { left: 930px; top: 140px; background: var(--paper); }
  .card-front .brand { position: absolute; top: 16px; left: 16px; }
  .card-front .brand-name { font-size: 14px; color: var(--charcoal); }
  .card-front .slogan { font-size: 6px; margin-top: 4px; }
  .card-front .person { position: absolute; top: 16px; right: 16px; text-align: right; }
  .card-front .person-name { font-size: 7px; font-weight: 600; color: var(--charcoal); }
  .card-front .person-role { font-size: 5.5px; color: var(--muted); margin-top: 2px; }
  .card-front .dark-band { height: 52px; align-items: stretch; }
  .card-front .contact { flex: 1; padding: 9px 16px; font-size: 5.5px; line-height: 1.6; white-space: nowrap; }
  .card-front .band-end { width: 48px; }

  .card-back { left: 930px; top: 284px; background: var(--charcoal); display: flex; align-items: center; justify-content: center; }
  .card-back .brand-name { font-size: 13px; color: var(--paper); }

  /* Envelopes */
  .envelope { width: 220px; height: 110px; }
  .envelope-front { left: 930px; top: 440px; background: var(--paper); }
  .envelope-front .brand { position: absolute; top: 14px; left: 14px; }
  .envelope-front .brand-name { font-size: 12px; color: var(--charcoal); }
  .envelope-front .slogan { font-size: 5px; margin-top: 3px; }
  .envelope-front .dark-band { height: 30px; font-size: 4.8px; }
  .envelope-front .band-text { flex: 1; padding-left: 14px; }
  .envelope-front .band-end { width: 40px; height: 100%; }

  .envelope-back { left: 930px; top: 580px; background: var(--paper-shade); }
  .envelope-back .flap { position: absolute; left: 0; right: 0; top: 0; height: 40px; background: var(--charcoal); display: flex; align-items: center; justify-content: center; }
  .envelope-back .brand-name { font-size: 8px; color: var(--paper); }
</style>
</head>
<body>

<section class="sheet letterhead">
  <div class="brand">
    <div class="brand-name">Brelix</div>
    <div class="slogan">Clear calls, fair prices, every day</div>
  </div>
  <div class="dark-band">
    <div class="band-start bubble-band" role="img" aria-label="Colourful speech bubble pattern"></div>
    <div class="band-text">4127 Harlow Pkwy, suite 410, Marlow TX 75318 &nbsp; T: 555-014-2297 &nbsp; F: 555-014-2297 &nbsp; brelix.example</div>
    <div class="band-end bubble-band" role="img" aria-label="Colourful speech bubble pattern"></div>
  </div>
</section>

<section class="sheet folder">
  <div class="brand">
    <div class="mark bubble-band"></div>
    <div class="brand-name">Brelix</div>
    <div class="slogan">Clear calls, fair prices, every day</div>
  </div>
  <div class="web">www.brelix.example</div>
</section>

<section class="sheet card card-front">
  <div class="brand">
    <div class="brand-name">Brelix</div>
    <div class="slogan">Clear calls, fair prices, every day</div>
  </div>
  <div class="person">
    <div class="person-name">Dana Reyes</div>
    <div class="person-role">Account Manager</div>
  </div>
  <div class="dark-band">
    <div class="contact">
      4127 Harlow Pkwy, suite 410<br>
      Marlow TX 75318<br>
      T: 555-014-2297 &nbsp; F: 555-014-2297<br>
      dana@brelix.example
    </div>
    <div class="band-end bubble-band" role="img" aria-label="Colourful speech bubble pattern"></div>
  </div>
</section>

<section class="sheet card card-back">
  <div class="brand-name">Brelix</div>
</section>

<section class="sheet envelope envelope-front">
  <div class="brand">
    <div class="brand-name">Brelix</div>
    <div class="slogan">Clear calls, fair prices, every day</div>
  </div>
  <div class="dark-band">
    <div class="band-text">4127 Harlow Pkwy, suite 410, Marlow TX 75318</div>
    <div class="band-end bubble-band" role="img" aria-label="Colourful speech bubble pattern"></div>
  </div>
</section>

<section class="sheet envelope envelope-back">
  <div class="flap">
    <div class="brand-name">Brelix</div>
  </div>
</section>

</body>
</html>
```